Site for company producing and selling products for children's health

We need an appealing professional web site design and images for a brand new company producing and selling products focused on children’s health. The site will offer information to visitors on the company, the company’s products, and general resources related to children’s health. Additionally the site will offer e-commerce functionality to allow for ordering of the company’s products.
The content and navigation for the site will be generated by programming, such as php or asp, and therefore any images used in the navigation portions of the site should allow for HTML markup to be overlaid rather than having the text built into the image or graphic.
The design must include 2 layouts, one for the landing/home page that includes only top navigation, and an inner page layout that includes both top and left navigation.
The header area of the site should include a place for links to access the visitor’s cart and profile similar to the top sections of plumvat.com, tidelor.com, and keenmart.com.
The landing page of the site should include some type of “changing” image area where we can include multiple image files for rotation to visitors similar to what is seen at vorta.com or brisksip.com. The flash/animation mechanism does not need to be provided (although it would be a plus if it was) but the design must accommodate the space for it.
The company’s colors are Orange (FF9900) and Blue (0066FF) and the logo can be viewed at http://wonkibrook.com/logo.png
All CSS and markup provided must be display consistently in Internet Explorer 7+, FifeFox, Google Chrome, and Safari.
Incorporating social media links (facebook, twitter, etc.) is desirable.
Parents who are conscious of health risks associated with children's diets and consumer food products.
E-Commerce

```html
<!DOCTYPE html>
<html lang="en">
<head>
<meta charset="utf-8">
<title>wonkibrook – Products</title>
<link rel="stylesheet" href="https://fonts.googleapis.com/css2?family=Arimo:wght@400;700&display=swap">
<style>
:root{
  --orange:#ff9900;
  --blue:#2266ee;
  --band:#3f7fe3;
  --text:#555;
  --dark:#222;
  --muted:#999;
  --line:#d8d8d8;
  --white:#fff;
  --hero-fill:#6aa6ec;
  --photo-fill:#a9c98a;
}
*{box-sizing:border-box;margin:0;padding:0}
html,body{width:1033px;height:1200px;overflow:hidden;background:var(--white);font-family:"Arimo",Arial,sans-serif;color:var(--text)}
.page{position:relative;width:1033px;height:1200px}
.abs{position:absolute}
a{color:inherit;text-decoration:none}

.top-rule{left:41px;top:2px;width:950px;height:4px;background:var(--orange)}
.brand{left:83px;top:72px;display:flex;align-items:center;gap:8px}
.brand-dot{width:22px;height:22px;border-radius:50%;background:var(--orange)}
.brand-name{font-size:27px;font-weight:700;color:var(--orange);letter-spacing:-.5px}

.account-links{right:62px;top:18px;font-size:12px;color:#333;display:flex;gap:16px;align-items:center}
.account-links .sep{color:#555}
.cart{display:flex;align-items:center;gap:6px}

.main-nav{left:371px;top:90px;height:31px}
.main-nav a{position:absolute;top:0;height:31px;background:var(--white);box-shadow:0 -2px 6px rgba(0,0,0,.15);border-radius:2px 2px 0 0;font-size:14px;color:#333;display:flex;align-items:center;justify-content:center}

.hero-band{left:41px;top:121px;width:950px;height:280px;background:var(--band)}
.hero-photo{left:46px;top:126px;width:724px;height:270px;background:var(--hero-fill)}
.search{left:791px;top:138px;width:180px;height:19px;background:var(--white);border:1px solid #ccc;font-size:10px;color:var(--muted);padding:3px 0 0 20px}
.search svg{position:absolute;right:8px;top:3px}
.slogan{left:631px;top:171px;width:340px;height:180px;background:rgba(255,255,255,.88);border:2px solid #c9d3e2;padding:28px 38px}
.slogan h2{font-size:18px;color:var(--blue);font-weight:700;margin-bottom:14px}
.slogan p{font-size:13px;line-height:17px;color:#aaa}
.btn{display:inline-block;background:var(--orange);color:var(--white);font-size:13px;padding:3px 10px;box-shadow:0 1px 2px rgba(0,0,0,.25)}
.slogan .btn{position:absolute;left:38px;top:138px;width:90px;height:22px}
.social{left:792px;top:366px;display:flex;gap:6px}
.social span{width:24px;height:24px;background:#dfe9f7;border:1px solid #b9cbe6;border-radius:3px}

.fade-strip{left:41px;top:401px;width:950px;height:62px;background:linear-gradient(#e4e4e4,#fff)}
.breadcrumb{left:274px;top:411px;font-size:10px;display:flex;gap:10px}
.breadcrumb .crumb{color:var(--blue)}
.breadcrumb .crumb a{text-decoration:underline}
.breadcrumb .current{color:var(--muted)}
.breadcrumb i{font-style:normal;margin-right:4px}

.side-nav{left:51px;top:461px;width:190px;border-top:1px solid var(--line)}
.side-nav li{list-style:none;border-bottom:1px solid var(--line);height:30px;display:flex;align-items:center;gap:8px;font-size:12px;color:#666}
.side-nav svg{flex:none}
.side-nav .sub{height:53px;display:block;padding:10px 0 0 18px;background:linear-gradient(#e8e8e8,#fff);font-size:12px;line-height:20px;color:#666;border-bottom:1px solid var(--line)}

.content{left:271px;top:458px;width:480px;font-size:12px;line-height:18px;color:var(--text)}
.content h1{font-size:18px;color:var(--blue);font-weight:700;margin-bottom:14px}
.content p{margin-bottom:18px}
.content h3{font-size:12px;color:var(--dark);font-weight:700;line-height:18px}
.content .inline{color:var(--blue);text-decoration:underline}
.content ul{list-style:none;margin:14px 0 16px 0}
.content li{position:relative;padding-left:15px;margin-bottom:3px}
.content li:before{content:"";position:absolute;left:0;top:6px;width:6px;height:6px;background:var(--blue)}

.side-photo{left:801px;top:503px;width:190px;height:123px;background:var(--photo-fill)}
.enlarge{left:809px;top:631px;font-size:11px;font-weight:700;font-style:italic;color:#777;display:flex;gap:4px;align-items:center}
.side-rule{left:801px;top:672px;width:190px;height:4px;background:var(--orange)}
.subscribe{left:801px;top:702px;width:190px}
.subscribe h2{font-size:18px;color:var(--blue);margin-bottom:18px}
.subscribe p{font-size:12px;line-height:18px;color:var(--text)}
.field{position:absolute;left:801px;width:180px;height:19px;border:1px solid #bbb;font-size:10px;color:var(--muted);padding:3px 10px}
.subscribe-btn{left:891px;top:899px;width:90px;height:22px;text-align:center}

.foot-rule{left:41px;top:947px;width:950px;height:4px;background:var(--orange)}
.foot-col{top:974px;font-size:12px;color:#999}
.foot-col h4{font-size:14px;font-weight:700;color:#999;margin-bottom:14px}
.foot-col li{list-style:none;line-height:20px;display:flex;gap:10px;align-items:center}
.foot-col .plain li{display:block;line-height:18px}
.foot-mark{left:842px;top:1022px;font-size:18px;font-weight:700;color:#c4c4c4}
.copyright{left:61px;top:1088px;font-size:11px;color:#999}
.foot-links{left:301px;top:1088px;font-size:11px;color:#999;display:flex;gap:12px}
</style>
</head>
<body>
<div class="page">
  <div class="abs top-rule"></div>

  <div class="abs brand"><span class="brand-dot"></span><span class="brand-name">wonkibrook</span></div>

  <nav class="abs account-links">
    <a href="#">My Account</a><span class="sep">|</span>
    <a href="#">Order Status</a><span class="sep">|</span>
    <a href="#" class="cart">
      <svg width="16" height="14" viewBox="0 0 16 14"><path d="M0 1h3l2 8h8l2-6H4" fill="none" stroke="#333" stroke-width="1.6"/><circle cx="6" cy="12" r="1.4" fill="#333"/><circle cx="12" cy="12" r="1.4" fill="#333"/></svg>
      Cart &nbsp;&nbsp;0 Items</a>
  </nav>

  <nav class="abs main-nav">
    <a href="#" style="left:0;width:80px">Home</a>
    <a href="#" style="left:90px;width:90px">About us</a>
    <a href="#" style="left:200px;width:80px">News</a>
    <a href="#" style="left:290px;width:95px">Products</a>
    <a href="#" style="left:400px;width:90px">Services</a>
    <a href="#" style="left:510px;width:90px">Contact</a>
  </nav>

  <div class="abs hero-band"></div>
  <div class="abs hero-photo" role="img" aria-label="Rotating banner photo placeholder: children playing outdoors"></div>
  <div class="abs search">Enter your search text
    <svg width="12" height="12" viewBox="0 0 12 12"><circle cx="5" cy="5" r="3.8" fill="none" stroke="#999" stroke-width="1.5"/><path d="M8 8l3 3" stroke="#999" stroke-width="1.8"/></svg>
  </div>
  <div class="abs slogan">
    <h2>Wonkibrook slogan goes here</h2>
    <p>orem ipsum dolor sit amet, consectetur adipiscing elit. Vivamus sit amet risus eu tellus consectetur</p>
    <a href="#" class="btn">Read more</a>
  </div>
  <div class="abs social"><span></span><span></span><span></span><span></span><span></span><span></span></div>

  <div class="abs fade-strip"></div>
  <div class="abs breadcrumb">
    <span class="crumb"><i>→</i><a href="#">home</a></span>
    <span class="crumb"><i>→</i><a href="#">products</a></span>
    <span class="crumb"><i>→</i><a href="#">productgroup one</a></span>
    <span class="current"><i>→</i>current page</span>
  </div>

  <ul class="abs side-nav">
    <li><svg width="13" height="13" viewBox="0 0 13 13"><circle cx="6.5" cy="6.5" r="5.6" fill="none" stroke="#777"/><path d="M3.5 6.5h6M7 4l2.5 2.5L7 9" fill="none" stroke="#777"/></svg>Product category one</li>
    <li style="border-bottom:none"><svg width="13" height="13" viewBox="0 0 13 13"><circle cx="6.5" cy="6.5" r="5.6" fill="none" stroke="#777"/><path d="M6.5 3.5v6M4 7l2.5 2.5L9 7" fill="none" stroke="#777"/></svg>Product category two</li>
    <li class="sub">Sub category one<br>Sub catergory two</li>
    <li><svg width="13" height="13" viewBox="0 0 13 13"><circle cx="6.5" cy="6.5" r="5.6" fill="none" stroke="#777"/><path d="M3.5 6.5h6M7 4l2.5 2.5L7 9" fill="none" stroke="#777"/></svg>Product category three</li>
    <li><svg width="13" height="13" viewBox="0 0 13 13"><circle cx="6.5" cy="6.5" r="5.6" fill="none" stroke="#777"/><path d="M3.5 6.5h6M7 4l2.5 2.5L7 9" fill="none" stroke="#777"/></svg>Product category four</li>
    <li><svg width="13" height="13" viewBox="0 0 13 13"><circle cx="6.5" cy="6.5" r="5.6" fill="none" stroke="#777"/><path d="M3.5 6.5h6M7 4l2.5 2.5L7 9" fill="none" stroke="#777"/></svg>Product category five</li>
    <li><svg width="13" height="13" viewBox="0 0 13 13"><circle cx="6.5" cy="6.5" r="5.6" fill="none" stroke="#777"/><path d="M3.5 6.5h6M7 4l2.5 2.5L7 9" fill="none" stroke="#777"/></svg>Product category six</li>
  </ul>

  <main class="abs content">
    <h1>Page title goes here</h1>
    <p>Lorem ipsum dolor sit amet, consectetur adipiscing elit. Pellentesque justo arcu, ultrices nec tincidunt ut, tempus ac felis. Vestibulum ante ipsum primis in faucibus orci luctus et ultrices posuere cubilia Curae; <a href="#" class="inline">Donec sed massa sem</a> ut venenatis dui. Nullam ullamcor-per lacus vel magna dignissim egestas. Sed sit amet velit a dolor sodales cursus. Sed convallis, urna tristique feugiat gravida, lectus libero vehicula erat, quis venenatis libero urna quis nunc. Nunc id tellus eget odio luctus molestie</p>
    <h3>Lorem ipsum dolar sit</h3>
    <p>Vestibulum in tellus tortor. Proin lorem urna, dignissim et facilisis aliquet, pharetra eu augue. Morbi pellentesque porttitor neque, vitae posuere risus faucibus ut. In hac habi-tasse platea dictumst. Ut ut nunc turpis. Donec non mi nisl. Donec nisl risus, pulvinar in ornare et, tincidunt vitae massa.</p>
    <ul>
      <li>Lorem ipsum dolar sit luctus non vulputate in, adipiscing eget ligula</li>
      <li>Phasellus diam turpis luctus non vulputate in, adipiscing eget ligula</li>
      <li>Luctus non vulputate in, adipiscing eget ligula</li>
    </ul>
    <p>In quis diam ac justo tempor pretium eu elementum tellus. Morbi eget dui ut ante ornare pulvinar. Sed dictum mattis felis, a dictum leo scelerisque sed. Quisque egestas, velit sed condimentum auctor, diam nulla tempus metus, a convallis nisi elit non ipsum. Phasellus vehicula rhoncus erat, sed viverra dolor consectetur vel.</p>
  </main>

  <div class="abs side-photo" role="img" aria-label="Product photo placeholder: children playing with soap bubbles outdoors"></div>
  <div class="abs enlarge"><svg width="12" height="12" viewBox="0 0 12 12"><circle cx="5" cy="5" r="4" fill="none" stroke="#777" stroke-width="1.5"/><path d="M3 5h4M5 3v4" stroke="#777"/><path d="M8 8l3 3" stroke="#777" stroke-width="1.8"/></svg>enlarge image</div>
  <div class="abs side-rule"></div>
  <section class="abs subscribe">
    <h2>Subscribe</h2>
    <p>Lorem ipsum dolor sit amet, con-sectetur adipiscing elit. Vivamus ...</p>
  </section>
  <div class="field" style="top:797px">Enter your name</div>
  <div class="field" style="top:841px">Enter your e-mail address</div>
  <a href="#" class="abs btn subscribe-btn">Subscribe</a>

  <div class="abs foot-rule"></div>
  <div class="abs foot-col" style="left:61px">
    <h4>Customer Service</h4>
    <ul><li>→ <span>Contact Us.</span></li><li>→ <span>Frequently Asked Questions.</span></li><li>→ <span>Return Policy Information.</span></li></ul>
  </div>
  <div class="abs foot-col" style="left:301px">
    <h4>My Account</h4>
    <ul><li>→ <span>Login/Register.</span></li><li>→ <span>My Account.</span></li><li>→ <span>Order Status</span></li></ul>
  </div>
  <div class="abs foot-col" style="left:521px;top:1005px">
    <ul class="plain"><li>Phone: 000 000 000</li><li>Fax: &nbsp;&nbsp;&nbsp;000 000 000</li><li>info@wonkibrook.com</li></ul>
  </div>
  <div class="abs foot-col" style="left:691px;top:1005px">
    <ul class="plain"><li>Address details</li><li>Address details</li><li>Country</li></ul>
  </div>
  <div class="abs foot-mark">wonkibrook</div>

  <div class="abs copyright">© 2010 Copyright wonkibrook</div>
  <nav class="abs foot-links">
    <a href="#">Home</a><span>|</span><a href="#">About us</a><span>|</span><a href="#">Services</a><span>|</span><a href="#">Products</a><span>|</span><a href="#">News</a><span>|</span><a href="#">Sitemap</a><span>|</span><a href="#">Contact us</a>
  </nav>
</div>
</body>
</html>
```